"Jewelry Line Postcard Design"

Would like to describe what the line is about via a bio include a photo of me and the logo.

Target Market(s)

20-55

Industry/Entity Type

Jewelry

```html
<!DOCTYPE html>
<html lang="en">
<head>
<meta charset="utf-8">
<title>Sora Vela – Dream Big Postcard</title>
<link rel="stylesheet" href="https://fonts.googleapis.com/css2?family=Cinzel:wght@400;700&family=PT+Sans:wght@400;700&family=PT+Sans+Narrow:wght@700&display=swap">
<style>
  :root {
    --stage: #1e1e1e;
    --card: #ffffff;
    --ink: #1a1a1a;
    --magenta: #c2278a;
    --banner-start: #c76fae;
    --banner-end: rgba(214, 150, 196, 0.35);
    --stamp: #f1dcef;
    --blush: #f6eef2;
    --portrait-light: #d9d9d9;
    --portrait-dark: #4a4a4a;
    --white: #ffffff;
  }
  * { box-sizing: border-box; margin: 0; padding: 0; }
  html, body { width: 1200px; height: 1000px; overflow: hidden; background: var(--stage); }
  body { position: relative; font-family: "PT Sans", sans-serif; color: var(--ink); }

  .postcard { position: absolute; background: var(--card); overflow: hidden; }

  /* Back of card */
  .postcard--back { left: 40px; top: 44px; width: 722px; height: 561px; }
  .back__photo-wash {
    position: absolute; inset: 0;
    background: radial-gradient(ellipse at 45% 30%, #ece3e3 0%, #f4eeee 40%, var(--blush) 70%, #fbf9fa 100%);
  }
  .back__stamp { position: absolute; left: 556px; top: 31px; width: 131px; height: 136px; background: var(--stamp); }
  .brand-name {
    position: absolute; font-family: "PT Sans", sans-serif; font-weight: 400;
    color: var(--ink); letter-spacing: 1px; display: flex; align-items: center; gap: 6px; white-space: nowrap;
  }
  .brand-name__mark { display: inline-block; background: var(--magenta); }
  .back__brand { left: 37px; top: 140px; font-size: 20px; }
  .back__brand .brand-name__mark { width: 8px; height: 8px; }
  .back__bio { position: absolute; left: 37px; top: 190px; width: 290px; font-size: 16px; line-height: 23.5px; }
  .name-banner {
    position: absolute; height: 27px;
    background: linear-gradient(90deg, var(--banner-start) 0%, var(--banner-start) 55%, var(--banner-end) 100%);
    color: var(--white); font-family: "PT Sans Narrow", sans-serif; font-weight: 700; font-size: 19px; line-height: 27px;
  }
  .back__banner { left: 0; top: 318px; width: 176px; padding-left: 38px; }
  .back__email { position: absolute; left: 38px; top: 356px; font-size: 16px; }
  .back__jewelry {
    position: absolute; left: 44px; top: 376px; width: 142px; height: 94px;
    background: radial-gradient(ellipse at center, #e4c98c 0%, #efe0bd 45%, rgba(246,238,242,0) 75%);
  }

  /* Front of card */
  .postcard--front { left: 431px; top: 400px; width: 754px; height: 584px; box-shadow: 0 0 18px rgba(0,0,0,0.35); }
  .front__splash {
    position: absolute; left: 120px; top: 200px; width: 340px; height: 384px;
    background: radial-gradient(ellipse at 50% 45%, rgba(190,170,225,0.55) 0%, rgba(235,190,225,0.4) 35%, rgba(245,220,235,0.15) 65%, rgba(255,255,255,0) 80%);
  }
  .front__portrait {
    position: absolute; left: 380px; top: 0; width: 374px; height: 584px;
    background: radial-gradient(ellipse at 55% 35%, var(--portrait-light) 0%, #a8a8a8 40%, var(--portrait-dark) 75%, #2c2c2c 100%);
    -webkit-mask-image: linear-gradient(90deg, transparent 0%, #000 30%);
    mask-image: linear-gradient(90deg, transparent 0%, #000 30%);
  }
  .front__brand { left: 56px; top: 56px; font-size: 26px; }
  .front__brand .brand-name__mark { width: 10px; height: 10px; }
  .front__headline { position: absolute; left: 222px; top: 64px; font-family: "Cinzel", serif; color: var(--ink); white-space: nowrap; }
  .front__headline-dream { font-size: 27px; font-weight: 400; }
  .front__headline-big { font-size: 44px; font-weight: 700; color: var(--magenta); margin-left: 6px; }
  .front__story { position: absolute; left: 42px; top: 138px; width: 436px; font-size: 14.6px; line-height: 20.5px; }
  .front__quote-mark { position: absolute; left: 30px; top: 268px; font-family: "Cinzel", serif; font-weight: 700; font-size: 96px; line-height: 1; }
  .front__quote { position: absolute; left: 97px; top: 270px; width: 330px; font-size: 18.5px; line-height: 24.6px; }
  .front__banner { left: 0; top: 435px; width: 218px; height: 33px; line-height: 33px; padding-left: 95px; }
  .front__signature { position: absolute; right: 42px; bottom: 36px; font-family: "Cinzel", serif; font-size: 23px; color: var(--white); letter-spacing: 1px; }
</style>
</head>
<body>

  <section class="postcard postcard--back" aria-label="Postcard back">
    <div class="back__photo-wash" role="img" aria-label="Faded portrait photo of the designer as background"></div>
    <div class="back__stamp"></div>
    <div class="brand-name back__brand"><span>SORA VELA</span><span class="brand-name__mark"></span></div>
    <p class="back__bio">Dr. Mara’s jewelry has been worn by stylists, designers, high profile TV personalities and anchors, as well as people who just want to look good and feel beautiful.</p>
    <div class="name-banner back__banner">Dr. Mara Linden</div>
    <p class="back__email">email: info@drmaralinden.com</p>
    <div class="back__jewelry" role="img" aria-label="Photo of gold earrings and statement necklace"></div>
  </section>

  <section class="postcard postcard--front" aria-label="Postcard front">
    <div class="front__splash" role="img" aria-label="Soft floral watercolor splash in lilac and pink"></div>
    <div class="front__portrait" role="img" aria-label="Black and white portrait photo of the designer"></div>
    <div class="brand-name front__brand"><span>SORA VELA</span><span class="brand-name__mark"></span></div>
    <h1 class="front__headline"><span class="front__headline-dream">DREAM</span><span class="front__headline-big">BIG</span></h1>
    <p class="front__story">This Collection was based on the bold and dramatic costume pieces of the 60's and 70's. The Jewelry collection was named Sora Vela, which means dream big in Romanian, because we all deserve to live out our biggest dreams!</p>
    <span class="front__quote-mark" aria-hidden="true">“</span>
    <blockquote class="front__quote">It’s my goal to make every woman feel like her very best self, so she can go out into the world to sparkle and shine. To create a line of jewelry that’s both beautiful and purposeful is truly a dream come true.”</blockquote>
    <div class="name-banner front__banner">Dr. Mara Linden</div>
    <p class="front__signature">DR. MARA</p>
  </section>

</body>
</html>
```